Convention Display

We need a convention booth design for an 10' W x 8' T booth. It should match the look and feel of our website and our brochure design. Sample design and text via 'upload files' below. www.fernmoorhaven.com

```html
<!DOCTYPE html>
<html lang="en">
<head>
<meta charset="utf-8">
<title>Fernmoor Haven – Convention Display</title>
<link rel="stylesheet" href="https://fonts.googleapis.com/css2?family=Roboto+Condensed:wght@700&family=Questrial&family=Satisfy&display=swap">
<style>
  :root {
    --green: #8dc63f;
    --blue: #1a75bb;
    --orange: #f7941d;
    --slate: #3f4b54;
    --ink: #231f20;
    --grey-text: #6d6e70;
    --grey-plus: #a7a9ac;
    --frame: #d3d3d3;
    --paper: #ffffff;
  }
  * { margin: 0; padding: 0; box-sizing: border-box; }
  html, body { width: 1200px; height: 848px; overflow: hidden; background: var(--paper); }
  .booth { position: relative; width: 1200px; height: 848px; font-family: "Questrial", sans-serif; }
  .booth-frame { position: absolute; left: 71px; top: 78px; width: 1063px; height: 639px; border: 1px solid var(--frame); }

  .photo { position: absolute; }
  .photo-doctor {
    left: 88px; top: 28px; width: 405px; height: 440px;
    background: radial-gradient(ellipse at 50% 30%, #c9c9c9 0%, #a9a9a9 35%, rgba(235,235,235,0.6) 70%, rgba(255,255,255,0) 100%);
  }
  .photo-model {
    left: 810px; top: 42px; width: 320px; height: 500px;
    background: radial-gradient(ellipse at 45% 35%, #bdbdbd 0%, #9a9a9a 30%, rgba(225,225,225,0.6) 68%, rgba(255,255,255,0) 100%);
  }

  .headline {
    position: absolute; left: 0; width: 1208px; top: 86px; text-align: center;
    font-family: "Roboto Condensed", sans-serif; font-weight: 700; font-size: 28px; color: var(--ink);
  }
  .headline .accent { color: var(--green); }

  .brand-name {
    position: absolute; left: 0; width: 1228px; top: 170px; text-align: center;
    font-family: "Questrial", sans-serif; font-size: 58px; color: var(--slate); letter-spacing: -1px;
  }
  .brand-tagline {
    position: absolute; left: 0; width: 1228px; top: 239px; text-align: center;
    font-size: 18px; color: var(--ink); letter-spacing: 0.5px;
  }

  .layer-badge {
    position: absolute; width: 126px; height: 126px; border-radius: 50%;
    display: flex; align-items: center; justify-content: center;
    font-family: "Satisfy", cursive; font-size: 50px; color: var(--paper); padding-bottom: 6px;
  }
  .badge-me { left: 188px; top: 351px; background: var(--green); }
  .badge-we { left: 548px; top: 351px; background: var(--blue); }
  .badge-info { left: 911px; top: 351px; background: var(--orange); font-size: 44px; }

  .plus { position: absolute; width: 46px; height: 46px; }
  .plus-one { left: 409px; top: 391px; }
  .plus-two { left: 756px; top: 391px; }

  .layer-title { position: absolute; width: 360px; top: 485px; text-align: center; font-size: 33px; }
  .title-personal { left: 74px; color: var(--green); }
  .title-shared { left: 419px; color: var(--blue); }
  .title-relevant { left: 790px; color: var(--orange); }

  .benefit {
    position: absolute; font-size: 25px; color: var(--grey-text); letter-spacing: -0.8px; white-space: nowrap;
  }
</style>
</head>
<body>
<main class="booth">
  <div class="booth-frame"></div>

  <div class="photo photo-doctor" role="img" aria-label="Black and white photo of a smiling doctor with a stethoscope holding out a smartphone"></div>
  <div class="photo photo-model" role="img" aria-label="Black and white photo of a smiling pregnant woman with long wavy hair"></div>

  <h1 class="headline"><span class="accent">3 LAYERS</span> TO ENGAGEMENT</h1>
  <p class="brand-name">fernmoor haven</p>
  <p class="brand-tagline">A NEW GENERATION PATIENT PORTAL</p>

  <div class="layer-badge badge-me">me</div>
  <svg class="plus plus-one" viewBox="0 0 46 46" aria-hidden="true"><rect x="17" y="0" width="12" height="46" fill="var(--grey-plus)"/><rect x="0" y="17" width="46" height="12" fill="var(--grey-plus)"/></svg>
  <div class="layer-badge badge-we">we</div>
  <svg class="plus plus-two" viewBox="0 0 46 46" aria-hidden="true"><rect x="17" y="0" width="12" height="46" fill="var(--grey-plus)"/><rect x="0" y="17" width="46" height="12" fill="var(--grey-plus)"/></svg>
  <div class="layer-badge badge-info">info</div>

  <p class="layer-title title-personal">make it personal</p>
  <p class="layer-title title-shared">make it shared</p>
  <p class="layer-title title-relevant">make it relevant</p>

  <p class="benefit" style="left:88px; top:570px;">Improve Satisfaction</p>
  <p class="benefit" style="left:200px; top:604px;">Integrate Your PHR</p>
  <p class="benefit" style="left:127px; top:638px;">Change Behavior</p>

  <p class="benefit" style="left:443px; top:570px;">Streamline Care</p>
  <p class="benefit" style="left:522px; top:604px;">Meet Meaningful Use</p>
  <p class="benefit" style="left:505px; top:638px;">Capture Analytics</p>

  <p class="benefit" style="left:795px; top:570px;">Increase Donations</p>
  <p class="benefit" style="left:906px; top:604px;">Incorporate Staff</p>
  <p class="benefit" style="left:822px; top:638px;">Grow Your Community</p>
</main>
</body>
</html>
```